Home Improvements Website

I would like a website that matches our business colour scheme and uses the fonts consistent without logo. (Monserrat, Chosence & Big Noddle Tiling).
We will need numerous sections: homepage, about us, services (with tiles or links to each service - building, landscaping, decking, maintenance, roofing, gutters etc) current projects (which must be easily editable by me, who is not too tech savvy) and a contacts page with enquiry form we can link to our job management service (Tradify).

```html
<!DOCTYPE html>
<html lang="en">
<head>
<meta charset="utf-8">
<title>Tallwood Home Improvements</title>
<link rel="stylesheet" href="https://fonts.googleapis.com/css2?family=Bebas+Neue&family=Montserrat:wght@400;500;600;700;800&display=swap">
<style>
:root{
  --green:#2e9e3a;
  --green-bright:#3db34a;
  --green-light:#8cc63f;
  --charcoal:#2f3331;
  --ink:#111211;
  --gold:#b99a63;
  --white:#ffffff;
  --text:#1d1d1d;
  --band:rgba(24,28,34,.72);
}
*{box-sizing:border-box;margin:0;padding:0}
html,body{width:1200px;height:3780px;overflow:hidden}
body{position:relative;background:var(--white);font-family:"Montserrat",sans-serif;color:var(--text)}
.abs{position:absolute}
.display{font-family:"Bebas Neue",sans-serif;font-weight:400;letter-spacing:1px}

/* header */
.site-header{position:absolute;left:0;top:0;width:1200px;height:94px;background:var(--white);border-top:3px solid var(--green-light);z-index:5}
.brand-badge{position:absolute;left:145px;top:0;width:160px;height:185px;background:var(--white);clip-path:polygon(0 0,100% 0,100% 78%,50% 100%,0 78%);display:flex;align-items:center;justify-content:center;gap:8px;z-index:6}
.brand-badge .mark{width:14px;height:14px;background:var(--green)}
.brand-badge .name{font-family:"Bebas Neue",sans-serif;font-size:30px;color:var(--charcoal);letter-spacing:1px}
.main-nav{position:absolute;left:470px;top:38px;display:flex;gap:35px;font-size:13px;font-weight:500;text-transform:uppercase}
.main-nav a{color:var(--text);text-decoration:none;padding-bottom:8px}
.main-nav a.active{border-bottom:2px solid var(--green)}
.search-icon{position:absolute;left:1040px;top:42px}

/* hero */
.hero-photo{position:absolute;left:0;top:94px;width:1200px;height:577px;background:linear-gradient(180deg,#3f6e3a 0%,#2d5a2f 35%,#8a9a86 60%,#cfd2c8 75%,#4f8a35 100%)}
.hero-title{position:absolute;left:360px;top:235px;width:478px;height:173px;background:rgba(35,35,35,.8);text-align:center;padding-top:12px}
.hero-title .top{font-size:78px;line-height:.95;color:var(--green-light)}
.hero-title .bottom{font-size:66px;line-height:1;color:var(--white)}
.play-button{position:absolute;left:573px;top:441px}

/* headings */
.section-title{position:absolute;width:1200px;text-align:center;font-size:60px;color:var(--ink)}

/* services */
.service-tile{position:absolute;width:396px;height:375px;overflow:hidden}
.service-tile .band{position:absolute;left:0;top:153px;width:100%;height:68px;background:var(--band);display:flex;align-items:center;justify-content:center;color:var(--white);font-weight:800;font-size:21px;text-transform:uppercase}
.service-tile .featured{position:absolute;left:68px;top:119px;width:260px;height:136px;background:rgba(46,158,58,.92);color:var(--white);text-align:center;padding-top:16px}
.featured h3{font-size:21px;font-weight:800;text-transform:uppercase}
.featured p{font-size:15px;margin-top:6px}
.featured .btn{display:inline-block;margin-top:12px;padding:6px 14px;border:2px solid var(--white);border-radius:20px;font-size:10px;font-weight:700;text-transform:uppercase}

/* about */
.about-text{position:absolute;left:544px;top:1945px;width:492px;font-size:13.6px;line-height:25.5px;color:var(--white);text-align:justify}
.outline-btn{position:absolute;border:2px solid var(--green-bright);border-radius:30px;color:var(--green-bright);background:var(--white);font-size:14px;font-weight:600;text-transform:uppercase;display:flex;align-items:center;justify-content:center;z-index:3}
.outline-btn.on-dark{background:transparent}

/* projects */
.project-tile{position:absolute}
.project-overlay{position:absolute;inset:0;background:rgba(80,200,90,.55);display:flex;align-items:center;justify-content:center}
.plus{width:40px;height:40px;border-radius:50%;background:var(--charcoal);color:var(--white);display:flex;align-items:center;justify-content:center;font-size:22px;margin-left:20px;margin-top:-10px}

/* footer */
.footer-brand{position:absolute;left:520px;top:3290px;width:160px;display:flex;align-items:center;justify-content:center;gap:8px}
.footer-brand .mark{width:14px;height:14px;background:var(--green-light)}
.footer-brand .name{font-family:"Bebas Neue",sans-serif;font-size:34px;color:var(--white);letter-spacing:1px}
.footer-heading{position:absolute;font-size:16px;font-weight:500;color:var(--white)}
.field{position:absolute;background:var(--white);font-size:10px;color:#555;padding:9px 10px;text-transform:uppercase}
.submit-btn{position:absolute;left:647px;top:3642px;width:82px;height:30px;border:2px solid var(--green-bright);border-radius:20px;color:var(--green-bright);font-size:12px;font-weight:600;display:flex;align-items:center;justify-content:center}
.contact-item{position:absolute;left:797px;display:flex;align-items:center;gap:17px;color:var(--white);font-size:12px;line-height:16px}
.contact-item .ic{width:34px;height:34px;border-radius:50%;border:2px solid var(--green-bright);display:flex;align-items:center;justify-content:center;flex-shrink:0}
.contact-item .ic.solid{background:var(--green-bright)}
.social{position:absolute;left:799px;top:3602px;display:flex;gap:8px}
.social span{width:27px;height:27px;border-radius:50%;background:var(--white)}
.social span.on{background:var(--green-bright)}
.divider{position:absolute;left:133px;top:3700px;width:935px;height:1px;background:#444}
.copyright{position:absolute;top:3732px;width:1200px;text-align:center;color:var(--white);font-size:12px}
</style>
</head>
<body>

<header class="site-header">
  <nav class="main-nav">
    <a class="active" href="#">Home</a>
    <a href="#">About Us</a>
    <a href="#">Services</a>
    <a href="#">Current Projects</a>
    <a href="#">Contact Us</a>
  </nav>
  <svg class="search-icon" width="14" height="14" viewBox="0 0 14 14"><circle cx="6" cy="6" r="4.5" fill="none" stroke="#3db34a" stroke-width="2"/><line x1="9.5" y1="9.5" x2="13" y2="13" stroke="#3db34a" stroke-width="2"/></svg>
</header>
<div class="brand-badge"><span class="mark"></span><span class="name">Tallwood</span></div>

<div class="hero-photo" role="img" aria-label="Suburban single-storey house with lawn, surrounded by tall pine trees"></div>
<svg class="abs" style="left:0;top:94px" width="1200" height="590" viewBox="0 0 1200 590">
  <polygon points="0,339 603,577 1200,330 1200,590 0,590" fill="#fff"/>
  <polyline points="0,339 603,577 1200,330" fill="none" stroke="#fff" stroke-width="14"/>
  <polyline points="0,346 603,584 1200,337" fill="none" stroke="#b99a63" stroke-width="6"/>
</svg>
<div class="hero-title"><div class="top display">Tallwood</div><div class="bottom display">Home Improvements</div></div>
<svg class="play-button" width="54" height="54" viewBox="0 0 54 54"><circle cx="27" cy="27" r="24" fill="#fff" stroke="#3db34a" stroke-width="4"/><polygon points="21,15 39,27 21,39" fill="#3db34a"/></svg>

<h2 class="section-title display" style="top:722px">Services</h2>
<div class="service-tile" style="left:0;top:818px;background:linear-gradient(160deg,#9fc0e0,#3f6e96 55%,#8fa38a)" role="img" aria-label="Glass office building">
  <div class="band">Building</div></div>
<div class="service-tile" style="left:402px;top:818px;background:linear-gradient(135deg,#5fa33a,#3d8a2a 50%,#8fb94a)" role="img" aria-label="Landscaped garden with winding stone path">
  <div class="featured"><h3>Landscaping</h3><p>Nemo enim ipluptatolupt</p><span class="btn">Read More</span></div></div>
<div class="service-tile" style="left:804px;top:818px;background:linear-gradient(180deg,#7ea6c8,#6a8a5a 40%,#9a7355 70%,#7a5a40)" role="img" aria-label="Timber deck with cable railings">
  <div class="band">Decking</div></div>
<div class="service-tile" style="left:0;top:1200px;background:linear-gradient(180deg,#c7a24a,#8a9a3a 35%,#6b3f25 60%,#4a2a18)" role="img" aria-label="Deck boards being stained with a brush">
  <div class="band">Maintenance</div></div>
<div class="service-tile" style="left:402px;top:1200px;background:linear-gradient(135deg,#6a8a4a,#8a8f95 35%,#2a76c0 60%,#6a7a5a)" role="img" aria-label="Aerial view of a house roof">
  <div class="band">Roofing</div></div>
<div class="service-tile" style="left:804px;top:1200px;background:linear-gradient(200deg,#2d5fa8,#5f86c0 45%,#d8dbe0 75%,#a8abb0)" role="img" aria-label="White gutter and downpipe on a house">
  <div class="band">Gutters</div></div>

<svg class="abs" style="left:0;top:1576px" width="1200" height="760" viewBox="0 0 1200 760">
  <defs>
    <linearGradient id="treeFill" x1="0" y1="0" x2="1" y2="0"><stop offset="0" stop-color="#1c9a3a"/><stop offset=".5" stop-color="#7bc142"/><stop offset="1" stop-color="#17a03a"/></linearGradient>
    <linearGradient id="collage" x1="0" y1="0" x2="1" y2="1"><stop offset="0" stop-color="#6f8f5a"/><stop offset=".5" stop-color="#8a5a38"/><stop offset="1" stop-color="#5a7a4a"/></linearGradient>
  </defs>
  <rect x="30" y="10" width="590" height="290" rx="60" fill="url(#treeFill)" role="img" aria-label="Illustration of trees and a house roof"/>
  <polygon points="27,272 1172,130 1172,602 27,749" fill="#2f3331"/>
  <circle cx="76" cy="342" r="11" fill="#fff"/><circle cx="76" cy="668" r="11" fill="#fff"/>
  <circle cx="1134" cy="212" r="11" fill="#fff"/><circle cx="1134" cy="539" r="11" fill="#fff"/>
  <polygon points="297,293 460,386 460,574 297,668 134,574 134,386" fill="none" stroke="#fff" stroke-width="2"/>
  <polygon points="297,306 450,394 450,566 297,655 144,566 144,394" fill="url(#collage)" role="img" aria-label="Collage of completed decks, gardens and homes"/>
</svg>
<h2 class="abs display" style="left:544px;top:1852px;font-size:56px;color:#fff">About Us</h2>
<p class="about-text">Sed ut perspiciatis unde omnis iste natus error sit voluptatem accusantium doloremque laudantium, totam rem aperiam, eaque ipsa quae ab illo inventore veritatis et quasi architecto beatae vitae dicta sunt explicabo. Nemo enim ipsam voluptatem quia voluptas sit aspernatur aut odit aut fugit, sed quia consequuntur magni dolores eos qui ratione voluptatem sequi nesque porro quisquam est,</p>
<div class="outline-btn on-dark" style="left:543px;top:2134px;width:137px;height:52px">Read More</div>

<h2 class="section-title display" style="top:2325px">Current Projects</h2>
<div class="project-tile" style="left:145px;top:2420px;width:300px;height:301px;background:linear-gradient(160deg,#3b6fd0,#8aa0c0 40%,#3a3f4a 70%,#c8ccd0)" role="img" aria-label="House siding with gutter and downpipe"></div>
<div class="project-tile" style="left:450px;top:2420px;width:605px;height:301px;background:linear-gradient(180deg,#4a7a4a,#2d6a2d)" role="img" aria-label="House surrounded by trees">
  <div class="project-overlay"><span class="plus">+</span></div></div>
<div class="project-tile" style="left:145px;top:2729px;width:300px;height:300px;background:linear-gradient(180deg,#5a7a7a,#2e5a2e 35%,#d8d4c8 55%,#4f9a35)" role="img" aria-label="Single-storey house with front lawn"></div>
<div class="project-tile" style="left:450px;top:2729px;width:300px;height:300px;background:linear-gradient(180deg,#7ab0e0,#4a7a3a 35%,#4fa02f)" role="img" aria-label="Freshly mown lawn with mower"></div>
<div class="project-tile" style="left:755px;top:2729px;width:300px;height:300px;background:linear-gradient(90deg,#2a6a2a,#3a7a2a 70%,#7a4a2a)" role="img" aria-label="Aerial view of turf and garden edging"></div>

<svg class="abs" style="left:0;top:3130px" width="1200" height="650" viewBox="0 0 1200 650">
  <defs><linearGradient id="footTrees" x1="0" y1="0" x2="1" y2="0"><stop offset="0" stop-color="#17a03a"/><stop offset=".5" stop-color="#8cc63f"/><stop offset="1" stop-color="#17a03a"/></linearGradient></defs>
  <polygon points="150,250 150,190 595,5 1170,240 1170,300 150,300" fill="url(#footTrees)" role="img" aria-label="Illustration of trees behind the footer"/>
  <polygon points="0,288 595,45 1200,288 1200,650 0,650" fill="#111211"/>
  <polyline points="0,280 595,37 1200,280" fill="none" stroke="#fff" stroke-width="8"/>
  <polyline points="0,288 595,45 1200,288" fill="none" stroke="#b99a63" stroke-width="6"/>
</svg>
<div class="outline-btn" style="left:531px;top:3068px;width:137px;height:54px">View More</div>
<div class="footer-brand"><span class="mark"></span><span class="name">Tallwood</span></div>

<div class="footer-heading" style="left:183px;top:3412px">Get In Touch</div>
<div class="field" style="left:185px;top:3449px;width:265px;height:29px">Name :</div>
<div class="field" style="left:462px;top:3449px;width:265px;height:29px">Phone :</div>
<div class="field" style="left:185px;top:3489px;width:542px;height:29px">Email :</div>
<div class="field" style="left:185px;top:3529px;width:542px;height:67px">Message :</div>
<div class="submit-btn">SUBMIT</div>

<div class="footer-heading" style="left:797px;top:3412px">Contact Information</div>
<div class="contact-item" style="top:3452px"><span class="ic"><svg width="12" height="16" viewBox="0 0 12 16"><path d="M6 0a6 6 0 0 1 6 6c0 4-6 10-6 10S0 10 0 6a6 6 0 0 1 6-6z" fill="#fff"/><circle cx="6" cy="6" r="2.2" fill="#111"/></svg></span><span>123,Nemo enim ipsam voluptatem<br>quia voluptdfs</span></div>
<div class="contact-item" style="top:3500px"><span class="ic solid"><svg width="14" height="14" viewBox="0 0 14 14"><path d="M3 1l2.5 3-1.5 1.5a8 8 0 0 0 4.5 4.5L10 8.5 13 11l-1.5 2C6 13 1 8 1 2.5z" fill="#fff"/></svg></span><span>+1 555 010 2040</span></div>
<div class="contact-item" style="top:3545px"><span class="ic"><svg width="14" height="11" viewBox="0 0 14 11"><rect width="14" height="11" rx="1" fill="#fff"/><polyline points="1,1 7,6 13,1" fill="none" stroke="#111" stroke-width="1.4"/></svg></span><span>hello@tallwoodhome.com</span></div>
<div class="social"><span></span><span class="on"></span><span></span><span></span></div>

<div class="divider"></div>
<p class="copyright">Copyrights © 2024, Tallwood Home Improvements. All Rights Reserved. &nbsp;|&nbsp; Privacy policy</p>

</body>
</html>
```